Endocrinologist needs new stationery

I have a logo from MarkForge and now need stationery with the new logo.

Address: Suite 4, 282 Falcon Street, Richmond, VIC 3121
Phone: 03 9417 2253
Fax: 03 9417 2255
Website: www.drmaylacorwen.com.au
Email: admin@drmaylacorwen.com.au

```html
<!DOCTYPE html>
<html lang="en">
<head>
<meta charset="utf-8">
<title>Dr Mayla Corwen – Presentation Folder</title>
<link href="https://fonts.googleapis.com/css2?family=Montserrat:wght@400&display=swap" rel="stylesheet">
<style>
  :root {
    --backdrop: #d9d8d9;
    --paper: #ffffff;
    --folder-blue: #24608f;
    --folder-blue-deep: #1f5482;
    --ink: #555358;
    --accent-blue: #2f6fa3;
    --accent-mauve: #7a5c6a;
    --silver: #d3d7dc;
  }
  html, body {
    margin: 0;
    padding: 0;
    width: 1200px;
    height: 847px;
    overflow: hidden;
    background: var(--backdrop);
    font-family: "Montserrat", sans-serif;
  }
  .spread {
    position: absolute;
    left: 119px;
    top: 84px;
    width: 962px;
    height: 680px;
    display: flex;
    box-shadow: 0 6px 24px rgba(0, 0, 0, 0.18);
  }
  .panel {
    position: relative;
    width: 481px;
    height: 680px;
  }
  .back-cover {
    background: var(--paper);
  }
  .front-cover {
    background: linear-gradient(160deg, var(--folder-blue) 0%, var(--folder-blue-deep) 100%);
  }
  .contact-block {
    position: absolute;
    left: 0;
    right: 0;
    bottom: 70px;
    text-align: center;
    color: var(--ink);
    font-size: 10.5px;
    line-height: 1.55;
    letter-spacing: 0.02em;
  }
  .contact-block p {
    margin: 0;
  }
  .contact-label--phone { color: var(--accent-blue); }
  .contact-label--fax { color: var(--accent-blue); }
  .contact-rule {
    width: 46px;
    height: 1px;
    background: var(--accent-mauve);
    margin: 4px auto 3px;
  }
  .contact-web {
    color: var(--ink);
  }
  .brand {
    position: absolute;
    right: 36px;
    bottom: 112px;
    display: flex;
    flex-direction: column;
    align-items: flex-end;
  }
  .brand-name {
    color: var(--silver);
    font-size: 19px;
    font-weight: 400;
    letter-spacing: 0.04em;
  }
  .brand-rule {
    width: 200px;
    height: 1px;
    background: var(--silver);
    margin-top: 7px;
    opacity: 0.8;
  }
</style>
</head>
<body>
  <main class="spread">
    <section class="panel back-cover">
      <div class="contact-block">
        <p><span class="contact-label--phone">T</span> : 03 9417 2253 <span class="contact-label--fax">F</span> : 03 9417 2255</p>
        <p>admin@drmaylacorwen.com.au</p>
        <p>Suite 4, 282 Falcon Street, Richmond, VIC 3121</p>
        <div class="contact-rule"></div>
        <p class="contact-web">www.drmaylacorwen.com.au</p>
      </div>
    </section>
    <section class="panel front-cover">
      <div class="brand">
        <span class="brand-name">Dr Mayla Corwen</span>
        <span class="brand-rule"></span>
      </div>
    </section>
  </main>
</body>
</html>
```